Flat bootstrap design for existing site

I'm looking for a modern flat design based around an existing logo. This has to be a custom design (no external templates), and implemented into a bootstrap framework.

The logo is attached as 2 versions - choose whichever you want, that flows better with whatever design you choose.

Added screenshots of the existing site (currently using the default bootstrap layouts). Please make your designs around those pages in the screenshots (i.e. the homepage only has the postal code input and the header). The active page has 3 screenshots, because I wanted to illustrate the other states that would be visible (in the table rows).

This is a moving/junk removal website, just for some context.

Here's some example websites (flat designs) that I like, just to give you an idea of what I'm after.

https://www.plivoterra.com/
https://damsoqua.com/
https://trevalin.com/
https://morkadelphi.com/en/

Coding

Coded - Design and coding required

Number of Pages Required

5+ page

Colors

Designer to choose colors to be used in the design.

Requirements
Must have
• It must be a modern/simple flat design, that is built around the existing logo (attached).
• It has to be implemented using bootstrap.

```html
<!DOCTYPE html>
<html lang="en">
<head>
<meta charset="utf-8">
<title>HAULNEST – Junk Removal</title>
<link rel="stylesheet" href="https://fonts.googleapis.com/css2?family=Roboto:wght@300;400;500;700;900&display=swap">
<style>
  :root{
    --sky:#4bc8f4;
    --sky-light:#8fe0fb;
    --sky-deep:#2fa6d6;
    --navy:#0b5f86;
    --navy-btn:#0a6c99;
    --white:#ffffff;
    --line:rgba(255,255,255,.35);
    --bezel:#111111;
    --gold:#d9c2a6;
    --screen:#f2f2f2;
  }
  *{margin:0;padding:0;box-sizing:border-box}
  html,body{width:1200px;height:789px;overflow:hidden}
  body{font-family:'Roboto',Arial,sans-serif;background:var(--sky);color:var(--white);position:relative}
  .waves{position:absolute;inset:0;width:1200px;height:789px}
  .site-header{position:absolute;left:0;top:0;width:1200px;height:97px;border-bottom:1px solid var(--line)}
  .brand{position:absolute;left:99px;top:30px;display:flex;align-items:center;gap:10px;font-weight:900;font-size:34px;letter-spacing:1px;color:var(--white)}
  .brand-dot{width:22px;height:22px;border-radius:50%;background:var(--white)}
  .main-nav{position:absolute;top:34px;left:444px;display:flex;align-items:center}
  .main-nav a{color:var(--white);text-decoration:none;font-size:17px;font-weight:400;letter-spacing:.2px}
  .nav-book{display:inline-flex;align-items:center;justify-content:center;width:86px;height:40px;border-radius:20px;background:var(--white);color:var(--sky)!important}
  .nav-how{margin-left:30px}
  .nav-driver{margin-left:30px}
  .nav-signin{margin-left:30px;display:inline-flex;align-items:center;gap:6px}
  .social{position:absolute;top:34px;left:1009px;display:flex;gap:14px}
  .social span{width:39px;height:39px;border:1.5px solid var(--white);border-radius:50%}
  .hero-title{position:absolute;top:136px;width:1200px;text-align:center;font-weight:700;font-size:61px;letter-spacing:-.5px;line-height:1}
  .hero-sub{position:absolute;top:205px;width:1200px;text-align:center;font-weight:700;font-size:51px;color:var(--navy);line-height:1}
  .hero-arrow{position:absolute;left:714px;top:224px}
  .booking{position:absolute;left:438px;top:284px;display:flex;gap:3px}
  .booking-input{width:247px;height:50px;border:1px solid var(--white);border-radius:25px 0 0 25px;padding-left:25px;display:flex;align-items:center;font-size:18px;color:var(--white);background:transparent}
  .booking-btn{width:93px;height:50px;border-radius:0 25px 25px 0;background:var(--navy-btn);display:flex;align-items:center;justify-content:center;font-weight:700;font-size:18px;letter-spacing:.5px}
  .deco{position:absolute;border-radius:18px;background:rgba(255,255,255,.18)}
  .deco-bin{left:197px;top:420px;width:129px;height:257px}
  .deco-recycle{left:874px;top:343px;width:163px;height:206px}
  .laptop{position:absolute;left:324px;top:360px;width:549px;height:377px;background:var(--bezel);border-radius:16px 16px 0 0;border:2px solid #cfcfcf}
  .laptop-screen{position:absolute;left:20px;top:26px;width:507px;height:317px;background:radial-gradient(circle at 50% 50%,#d7ebc4 0,#f5f5f5 38%,#efefef 100%)}
  .laptop-base{position:absolute;left:261px;top:733px;width:673px;height:13px;background:linear-gradient(var(--gold),#a58e74);border-radius:2px 2px 10px 10px}
  .play-btn{position:absolute;left:758px;top:660px;width:80px;height:34px;border:1px solid var(--sky);border-radius:17px;background:var(--white);color:var(--sky);font-size:13px;font-weight:500;display:flex;align-items:center;padding-left:13px;gap:16px}
</style>
</head>
<body>
  <svg class="waves" viewBox="0 0 1200 789" aria-hidden="true">
    <path d="M0 520 C120 500 220 560 330 590 C480 630 600 600 760 560 C900 525 980 420 1200 470 L1200 789 L0 789Z" fill="#43bdea"/>
    <path d="M760 789 C860 700 980 560 1200 470 L1200 789Z" fill="var(--sky-deep)"/>
    <path d="M0 640 C160 600 300 700 420 730 C600 770 760 700 900 760 L900 789 L0 789Z" fill="var(--sky-light)" opacity=".7"/>
    <path d="M0 600 C200 560 320 680 480 700 C640 720 760 640 900 650" stroke="rgba(255,255,255,.3)" fill="none"/>
  </svg>

  <header class="site-header">
    <div class="brand"><span class="brand-dot"></span>HAULNEST</div>
    <nav class="main-nav">
      <a class="nav-book" href="#">BOOK</a>
      <a class="nav-how" href="#">HOW IT WORKS</a>
      <a class="nav-driver" href="#">BECOME A DRIVER</a>
      <a class="nav-signin" href="#">SIGN IN
        <svg width="12" height="12" viewBox="0 0 12 12" fill="none" stroke="#fff" stroke-width="1.4"><path d="M1 6h7M5.5 3l3 3-3 3M11 1v10"/></svg>
      </a>
    </nav>
    <div class="social"><span></span><span></span></div>
  </header>

  <h1 class="hero-title">Need Junk Removed?</h1>
  <p class="hero-sub">BOOK NOW.</p>
  <svg class="hero-arrow" width="50" height="46" viewBox="0 0 50 46" fill="none" stroke="#fff" stroke-width="1.5" aria-hidden="true">
    <path d="M2 8 C20 0 36 8 44 34"/><path d="M36 28 L44 38 L48 26"/>
  </svg>

  <form class="booking">
    <div class="booking-input">Postal Code</div>
    <div class="booking-btn">BOOK</div>
  </form>

  <div class="deco deco-bin" role="img" aria-label="Outline drawing of a tipped waste bin"></div>
  <div class="deco deco-recycle" role="img" aria-label="Outline recycling arrows"></div>

  <div class="laptop">
    <div class="laptop-screen" role="img" aria-label="Video still: recycling symbol surrounded by line icons of household junk"></div>
  </div>
  <div class="laptop-base"></div>
  <div class="play-btn">Play
    <svg width="12" height="14" viewBox="0 0 12 14"><path d="M0 0L12 7L0 14Z" fill="#4bc8f4"/></svg>
  </div>
</body>
</html>
```